Webdesign für ein Dachdeckerbetrieb
Zielgruppe
Wir sind ein Dachdeckerbetrieb.
Zielgruppe sind öffentliche Auftrageber , Hausverwaltungen und private Hausbesitzer.
Aufgabenstellung
Die Seite sollte übersichtlich sein. Nicht zuviele Menüs durch die man klicken muss.
Bilder können wir liefern .
Nach Vorgabe des Designers beschaffen wir die Bilder .
Logo ist vorhanden.

```html
<!DOCTYPE html>
<html lang="de">
<head>
<meta charset="utf-8">
<title>Kranholt Dachbau – Dachdecker und Zimmerer</title>
<link rel="stylesheet" href="https://fonts.googleapis.com/css2?family=Source+Sans+3:wght@400;600;700&display=swap">
<style>
:root{
  --green:#94b026;
  --green-soft:#d4e0a8;
  --ink:#3a3a3a;
  --muted:#6b6b6b;
  --light:#9a9a9a;
  --white:#ffffff;
}
*{margin:0;padding:0;box-sizing:border-box}
html,body{width:1200px;height:2612px;overflow:hidden;background:var(--white)}
body{font-family:"Source Sans 3",sans-serif;color:var(--ink);position:relative}
.abs{position:absolute}
.header{top:0;left:0;width:1200px;height:82px}
.brand{left:196px;top:22px;display:flex;align-items:center;gap:8px;font-weight:700;font-size:16px;line-height:17px;color:var(--green);white-space:nowrap}
.brand-mark{width:14px;height:14px;background:var(--green);flex:none}
.header-phone{left:331px;top:36px;font-size:12px;color:var(--muted);white-space:nowrap}
.nav{left:583px;top:36px;display:flex;gap:36px;font-size:13px;font-weight:600}
.nav a,.footer-nav a{color:var(--ink);text-decoration:none}
.btn-outline-green{left:940px;top:31px;width:66px;height:27px;border:1px solid var(--green);border-radius:14px;color:var(--green);font-size:12px;font-weight:600;display:flex;align-items:center;justify-content:center}
.hero{top:82px;left:0;width:1200px;height:376px;background:linear-gradient(120deg,#a7c24b 0%,#9dba3d 55%,#8fa937 100%)}
.hero-title{top:216px;left:0;width:1200px;text-align:center;color:var(--white);font-size:33px;font-weight:700;line-height:39px}
.btn-outline-white{border:1px solid var(--white);border-radius:18px;color:var(--white);font-size:12px;font-weight:600;display:flex;align-items:center;justify-content:center}
.hero-btn{left:527px;top:316px;width:147px;height:34px}
.hero-band{top:458px;left:0;width:1200px;height:38px;background:var(--green-soft)}
.services{top:438px;left:260px;width:674px;height:104px;background:#fcfcfb;border-radius:6px;box-shadow:0 4px 14px rgba(0,0,0,.07);display:flex;padding:24px 0 0 34px}
.services ul{list-style:none;width:204px;font-size:12.5px;color:var(--muted);line-height:17.5px}
.services li::before{content:"";display:inline-block;width:4px;height:4px;border-radius:50%;background:var(--green);margin:0 10px 2px 0}
.intro{top:630px;left:260px;width:650px;font-size:17.5px;line-height:25px;color:var(--ink)}
.photo-roof{left:196px;top:795px;width:398px;height:269px;background:linear-gradient(160deg,#7aa0c4 0%,#3c4a5e 45%,#c9a67a 100%)}
.photo-roofer{left:606px;top:1140px;width:398px;height:269px;background:linear-gradient(170deg,#b9cde0 0%,#8aa8c6 40%,#2f3a4b 75%,#9d7b58 100%)}
.photo-hammer{left:196px;top:1490px;width:398px;height:270px;background:linear-gradient(175deg,#c9d2c4 0%,#6b7f4d 35%,#c49a6c 65%,#d9d6d0 100%)}
.feature h2{font-size:24px;font-weight:700;line-height:28px;color:var(--ink)}
.feature p{margin-top:22px;font-size:11px;line-height:15.6px;color:var(--ink)}
.checks{list-style:none;margin-top:16px;font-size:11px;line-height:17.5px}
.checks li{display:flex;align-items:center;gap:6px}
.btn-green{background:var(--green);color:var(--white);border-radius:18px;font-size:11.5px;font-weight:600;display:flex;align-items:center;justify-content:center}
.feature-one{left:675px;top:796px;width:260px}
.feature-two{left:262px;top:1173px;width:262px}
.feature-three{left:678px;top:1523px;width:250px}
.partners-title{top:1880px;left:0;width:1212px;text-align:center;font-size:19px;font-weight:600}
.partners{top:1930px;left:264px;width:676px;display:flex;justify-content:space-between;align-items:center}
.badge{height:22px;background:#2e2e38;border-radius:4px}
.cta{top:2038px;left:0;width:1200px;height:269px;background:var(--green)}
.cta-text{top:2111px;left:0;width:1212px;text-align:center;color:var(--white);font-size:24.5px;line-height:35px}
.cta-btn{left:533px;top:2200px;width:147px;height:34px}
.footer-address{left:263px;top:2390px;font-size:11px;line-height:15.5px;font-style:normal}
.footer-address strong{font-weight:700}
.footer-address a{color:var(--ink)}
.footer-nav{left:607px;top:2390px;font-size:12px;font-weight:600;display:flex;flex-direction:column;gap:7px}
.footer-brand{left:842px;top:2414px}
.legal{left:263px;top:2541px;display:flex;gap:22px;font-size:9.5px;color:var(--light)}
</style>
</head>
<body>
<header class="abs header">
  <div class="abs brand"><span class="brand-mark"></span><span>Kranholt<br>Dachbau</span></div>
  <div class="abs header-phone">06100 - 24 57 80</div>
  <nav class="abs nav"><a href="#">Leistungen</a><a href="#">Über uns</a><a href="#">Referenzen</a></nav>
  <a class="abs btn-outline-green">Anfrage</a>
</header>

<section class="abs hero" role="img" aria-label="Dachdecker bei der Arbeit auf einem Dach, grün eingefärbt"></section>
<h1 class="abs hero-title">Starke und zuverlässige Dachdecker und<br>Zimmerer für Ihre Dachsanierung</h1>
<a class="abs btn-outline-white hero-btn">Angebot einholen</a>
<div class="abs hero-band"></div>

<div class="abs services">
  <ul><li>Ziegeldach</li><li>Flachdach</li><li>Abdichtungstechnik</li></ul>
  <ul><li>Reparaturen &amp; Wartung</li><li>Bauklempnerei</li><li>Stehfalzarbeiten</li></ul>
  <ul style="margin-top:-3px"><li>Dacherneuerungen</li><li>Dachumbauten</li><li>Einbau von Dachflächenfenstern</li></ul>
</div>

<p class="abs intro">Wir helfen Ihnen persönliche Wünsche mit technisch und fachlich richtigen Lösungen umzusetzen. Egal, ob Sie eine Neueindeckung oder eine Sanierung Ihres Wohnhauses wünschen, eine Wärmedämmung nach den neuesten gesetzlichen Vorgaben umgesetzt oder ein Dachfenster eingebaut werden soll.</p>

<div class="abs photo-roof" role="img" aria-label="Dachdecker auf einem Gerüst an einem neu eingedeckten Ziegeldach"></div>
<div class="abs feature feature-one">
  <h2>Für ein sicheres und langlebiges Zuhause</h2>
  <p>Unsere erfahrene Dachdecker und Zimmerer bauen Ihnen ein qualitativ hochwertiges Dach, das Sie bei „Wind und Wetter“ schützt und Ihnen ein sicheres und langlebiges Zuhause bietet.</p>
  <ul class="checks">
    <li><svg width="12" height="10" viewBox="0 0 12 10"><path d="M1 5l3.5 3.5L11 1" fill="none" stroke="#94b026" stroke-width="1.6"/></svg>Langjährige Erfahrung</li>
    <li><svg width="12" height="10" viewBox="0 0 12 10"><path d="M1 5l3.5 3.5L11 1" fill="none" stroke="#94b026" stroke-width="1.6"/></svg>Erfüllung gesetzlicher Vorgaben</li>
    <li><svg width="12" height="10" viewBox="0 0 12 10"><path d="M1 5l3.5 3.5L11 1" fill="none" stroke="#94b026" stroke-width="1.6"/></svg>Ausführliche Beratung zu allen Fragen</li>
  </ul>
</div>
<a class="abs btn-green" style="left:676px;top:1017px;width:146px;height:35px">Unsere Leistungen</a>

<div class="abs feature feature-two">
  <h2>Aus Überzeugung und Freude am Tun</h2>
  <p>Der Herausforderung ein Steildach, Ziegeldach oder Flachdach fachmännisch zu decken, stellen wir uns täglich gerne. Wir nehmen Ihre Wünsche in unserer anschließenden Planung auf und erarbeiten mit Ihnen und für Sie die optimale Lösung.</p>
</div>
<a class="abs btn-green" style="left:262px;top:1346px;width:125px;height:33px">Mehr über uns</a>
<div class="abs photo-roofer" role="img" aria-label="Dachdecker steht auf dem Gerüst vor einem Ziegeldach und Solaranlage"></div>

<div class="abs photo-hammer" role="img" aria-label="Hammer auf einer Mauer vor einem Dachstuhl aus Holzlatten"></div>
<div class="abs feature feature-three">
  <h2>Fachbetrieb und zuverlässiger Partner</h2>
  <p>Unser Fachbetrieb ist Ihr zuverlässiger und fachkundiger Partner in allen Fragen rund um das Thema Bedachungen. Wir unterstützen Sie bei der Planung und Durchführung von sämtlichen Dachdeckerarbeiten.</p>
</div>
<a class="abs btn-green" style="left:679px;top:1701px;width:116px;height:34px">Referenzen</a>

<h2 class="abs partners-title">Unsere Partner</h2>
<div class="abs partners">
  <div class="badge" style="width:86px"></div>
  <div class="badge" style="width:104px"></div>
  <div class="badge" style="width:82px"></div>
  <div class="badge" style="width:96px"></div>
</div>

<section class="abs cta"></section>
<p class="abs cta-text">Solides Handwerk und Können ist eine Sache, Vertrauen eine andere.<br>Wir sind Ihr Partner für ausdrucksstarke und sichere Dächer.</p>
<a class="abs btn-outline-white cta-btn">Angebot einholen</a>

<address class="abs footer-address">
  <strong>Kranholt Dachbau</strong><br>Lindenweg 12<br>55999 Musterheim<br>
  <span style="display:block;height:14px"></span>
  <a href="#">info@kranholt-dachbau.example</a><br>
  <a href="#" style="line-height:22px">06100 - 24 57 80</a>
</address>
<nav class="abs footer-nav"><a href="#">Leistungen</a><a href="#">Über uns</a><a href="#">Referenzen</a><a href="#">Anfrage</a></nav>
<div class="abs brand footer-brand"><span class="brand-mark"></span><span>Kranholt<br>Dachbau</span></div>
<div class="abs legal"><span>Impressum</span><span>Datenschutz</span></div>
</body>
</html>
```